Kelmori.com.au - AV and Communications Installation Company Website

A company website for a modern, high level/enterprise communications installation/engineering company based in Sydney Australia.
My client base is construction companies working in medical, government and educations departments so the website needs to look professional.
Clients like Brisle or Torvex as I want to eventually move into data centre design and installation so I need something appealing to the high end market.
Fiber Optic Installation is a massive part of the company aswell.
Audio visual, IT installation is also what the company will be involved in.
I want the website to be modern, eye catching, professional looking.

Target Market(s)

High end clients and construction companies

Industry/Entity Type

Communications

Coding

Coded - Design and coding required

Number of Pages Required

1 page

Requirements
Must have
• Modern and clean layout with links to other social media platforms

```html
<!DOCTYPE html>
<html lang="en">
<head>
<meta charset="utf-8">
<title>Kelmori – Enterprise Communications Installation</title>
<link href="https://fonts.googleapis.com/css2?family=Montserrat:wght@500;600;700&family=Open+Sans:wght@400;600;700&display=swap" rel="stylesheet">
<style>
:root{
  --teal:#1b7f8c;
  --teal-bright:#2a9aa8;
  --slate:#58585b;
  --ink:#1d1d1f;
  --muted:#555;
  --white:#fff;
  --light:#f4f4f4;
  --footer:#232323;
}
*{margin:0;padding:0;box-sizing:border-box}
html,body{width:1200px;height:4591px;overflow:hidden}
body{position:relative;font-family:"Open Sans",Arial,sans-serif;color:var(--ink);background:var(--white)}
.abs{position:absolute}
a{color:inherit;text-decoration:none}

/* header */
.site-header{position:absolute;top:0;left:0;width:1200px;height:84px;background:var(--white);border-top:4px solid var(--teal);z-index:2}
.brand{position:absolute;left:90px;top:16px;display:flex;align-items:center;gap:12px;font-family:"Montserrat",sans-serif;font-weight:600;font-size:36px;line-height:48px;color:var(--teal);letter-spacing:1px}
.brand-dot{width:18px;height:18px;border-radius:50%;background:var(--teal)}
.main-nav{position:absolute;right:90px;top:32px;display:flex;gap:40px;font-size:14px;font-weight:600;color:#222}
.main-nav .active{color:var(--teal);text-decoration:underline}

/* hero */
.hero{position:absolute;top:84px;left:0;width:1200px;height:1109px;
  background:linear-gradient(180deg,#27304a 0%,#3a3f5c 30%,#7a4a3a 48%,#c66a2e 53%,#3c3a44 60%,#2a2f44 100%)}
.hero-brand{position:absolute;top:148px;width:100%;text-align:center;font-family:"Montserrat",sans-serif;font-weight:600;font-size:100px;line-height:100px;color:var(--white);letter-spacing:3px}
.hero-tag{position:absolute;top:266px;width:100%;text-align:center;font-size:23px;line-height:35px;color:var(--white)}
.btn{display:inline-flex;align-items:center;justify-content:center;border-radius:30px;font-weight:700}
.btn-teal{background:var(--teal);color:var(--white)}
.btn-white{background:var(--white);color:var(--teal)}
.hero-cta{left:494px;top:363px;width:212px;height:52px;font-size:19px}
.welcome{position:absolute;top:722px;width:100%;text-align:center;font-family:"Montserrat",sans-serif;font-weight:700;font-size:48px;line-height:58px;color:var(--white)}
.welcome span{color:var(--teal-bright)}
.welcome-text{position:absolute;top:792px;left:140px;width:920px;text-align:center;font-size:16px;line-height:31px;color:#f0f0f0}
.hero-read{left:429px;top:951px;width:162px;height:48px;font-size:16px}
.hero-contact{left:609px;top:951px;width:162px;height:48px;font-size:16px}

/* clients */
.section-title{position:absolute;width:100%;text-align:center;font-family:"Montserrat",sans-serif;font-weight:700;font-size:44px;line-height:54px;color:var(--ink)}
.section-title span{color:var(--teal)}
.clients-title{top:1286px}
.diamonds{position:absolute;top:1366px;left:0}
.client{position:absolute;width:290px;text-align:center;color:var(--white)}
.client h3{font-size:22px;line-height:30px;font-weight:600;margin-bottom:6px}
.client p{font-size:14px;line-height:30px}

/* services */
.service{position:absolute;color:var(--white)}
.service h3{font-family:"Montserrat",sans-serif;font-weight:500;font-size:30px;line-height:42px;margin-bottom:24px}
.service p{font-size:16px;line-height:34px}
.service .arrow{margin-top:22px;font-size:24px}
.panel-teal{left:0;top:1940px;width:487px;height:344px;background:var(--teal);padding:38px 30px 0 90px}
.panel-slate{left:720px;top:2284px;width:480px;height:344px;background:var(--slate);padding:38px 70px 0 34px}
.photo{position:absolute}
.photo-fiber{left:487px;top:1940px;width:713px;height:344px;background:linear-gradient(120deg,#6f7a83 0%,#b9bfc2 35%,#2a4f8f 60%,#d6d8da 100%)}
.photo-cable{left:0;top:2284px;width:720px;height:344px;background:linear-gradient(135deg,#e9eaec 0%,#c7ccd0 45%,#d9b48c 70%,#e8e2a0 100%)}

/* testimonials */
.testi-title{top:2722px}
.card{position:absolute;top:2838px;width:319px;height:243px;background:var(--white);border-radius:18px;box-shadow:0 8px 22px rgba(0,0,0,.12);padding:46px 12px 0 34px}
.card h4{font-size:20px;line-height:26px;font-weight:400;margin-bottom:12px}
.card p{font-size:13.5px;line-height:27px;color:var(--muted);white-space:nowrap}
.card a{display:inline-block;margin-top:6px;font-size:14px;font-weight:700;color:var(--teal);text-decoration:underline}
.quote-badge{position:absolute;top:-26px;left:36px;width:50px;height:50px;background:var(--teal)}
.slider-arrow{position:absolute;top:2948px;font-size:28px;color:#555}

/* gallery */
.gallery{position:absolute;top:3209px;left:0;width:1200px;height:960px;background:var(--light)}
.gallery-title{top:92px}
.tile{position:absolute;width:244px;height:289px}
.view-all{left:519px;top:806px;width:162px;height:47px;font-size:16px}

/* footer */
.site-footer{position:absolute;top:4169px;left:0;width:1200px;height:422px;background:var(--footer);color:#e6e6e6}
.footer-brand{position:absolute;top:52px;width:100%;display:flex;justify-content:center;align-items:center;gap:12px;font-family:"Montserrat",sans-serif;font-weight:600;font-size:40px;line-height:50px;color:var(--teal-bright)}
.footer-nav{position:absolute;top:140px;width:100%;display:flex;justify-content:center;gap:46px;font-size:16px}
.contact{position:absolute;top:196px;width:300px;text-align:center;font-size:15px;line-height:24px}
.contact .icon{width:58px;height:58px;border-radius:50%;margin:0 auto 20px;background:#4b4b4b;display:flex;align-items:center;justify-content:center}
.contact .icon.is-active{background:#1ea5e6}
.copyright{position:absolute;top:376px;width:100%;text-align:center;font-size:12px;color:#ddd}
</style>
</head>
<body>

<header class="site-header">
  <div class="brand"><span class="brand-dot"></span>Kelmori</div>
  <nav class="main-nav">
    <a class="active" href="#">HOME</a><a href="#">ABOUT US</a><a href="#">SERVICES</a><a href="#">WORK</a><a href="#">SOLUTION</a><a href="#">CONTACT US</a>
  </nav>
</header>

<section class="hero" role="img" aria-label="Night view of Sydney harbour with the opera house and bridge at dusk">
  <div class="hero-brand">Kelmori</div>
  <p class="hero-tag">We are a high level ,enterprise communications<br>installation,engineering company</p>
  <a class="btn btn-teal abs hero-cta" href="#">Get Started</a>
  <h1 class="welcome">WELCOME TO <span>KELMORI</span></h1>
  <p class="welcome-text">Lorem ipsum dolor sit amet, consectetur adipiscing elit, sed do eiusmod tempor incididunt ut labore et dolore magna aliqua. Ut enim ad minim veniam, quis nostrud exercitation ullamco laboris nisi ut aliquip ex ea commodo consequat. Duis aute irure dolor in reprehenderit in voluptate velit esse cillum dolore eu fugiat nulla pariatur. Excepteur sint occaecat cupidatat non proident, sunt in culpa qui officia deserunt mollit anim id est laborum</p>
  <a class="btn btn-teal abs hero-read" href="#">Read More</a>
  <a class="btn btn-white abs hero-contact" href="#">Contact Us</a>
</section>

<h2 class="section-title clients-title">OUR <span>CLIENTS</span></h2>
<svg class="diamonds" width="1200" height="464" viewBox="0 0 1200 464">
  <polygon points="250,0 482,232 250,464 18,232" fill="#58585b"/>
  <polygon points="950,0 1182,232 950,464 718,232" fill="#58585b"/>
  <polygon points="600,0 832,232 600,464 368,232" fill="#1b7f8c"/>
  <g fill="none" stroke="#fff" stroke-width="2.5">
    <rect x="238" y="92" width="24" height="56" rx="4"/>
    <line x1="226" y1="120" x2="274" y2="120"/>
    <rect x="582" y="88" width="36" height="26" rx="3"/>
    <path d="M574 150 L626 150 L626 128 L574 128 Z"/>
    <line x1="600" y1="114" x2="600" y2="128"/>
    <path d="M950 148 C932 124 934 92 950 92 C966 92 968 124 950 148 Z"/>
    <circle cx="950" cy="110" r="6"/>
    <path d="M930 150 L970 150"/>
  </g>
</svg>
<div class="client" style="left:105px;top:1544px"><h3>Medical</h3><p>Lorem ipsum dolor sit amet, consectetur adipiscing elit, sed do mod tempor incididunt ut labore et dolore</p></div>
<div class="client" style="left:452px;top:1544px"><h3>Government</h3><p>Lorem ipsum dolor sit amet, consectetur adipiscing elit, sed do eiusmod tempor incididunt ut labore et dolore magna aliqua.</p></div>
<div class="client" style="left:813px;top:1544px"><h3>Education</h3><p>Lorem ipsum dolor sit amet, consectetur adipiscing elit, sed do eiusmod tempor incididunt ut</p></div>

<div class="service panel-teal">
  <h3>Fiber Optic<br>Installation</h3>
  <p>Lorem ipsum dolor sit amet, consectetur aing elit, sed do eiusmod tempor incididunt ut labore et dolore magna aliqua. ut aliquip ex ea cmodo consequat</p>
  <div class="arrow">&#10230;</div>
</div>
<div class="photo photo-fiber" role="img" aria-label="Technicians in hard hats working on a fiber optic patch cabinet"></div>
<div class="photo photo-cable" role="img" aria-label="Hand holding colourful fiber optic strands beside a splice tray"></div>
<div class="service panel-slate">
  <h3>Audio visual,<br>IT installation</h3>
  <p>Lorem ipsum dolor sit amet, consectetur aing elit, sed do eiusmod tempor incididunt ut labore et dolore magna aliqua.</p>
  <div class="arrow">&#10230;</div>
</div>

<h2 class="section-title testi-title">TESTIMONIALS</h2>
<div class="slider-arrow" style="left:38px">&#8249;</div>
<div class="slider-arrow" style="left:1148px">&#8250;</div>
<article class="card" style="left:91px">
  <svg class="quote-badge" viewBox="0 0 50 50"><rect width="50" height="50" fill="#1b7f8c"/><path d="M14 32v-8c0-5 3-8 7-8v4c-2 0-3 1-3 4h3v8zM28 32v-8c0-5 3-8 7-8v4c-2 0-3 1-3 4h3v8z" fill="#fff"/></svg>
  <h4>Samantha J</h4><p>Lorem ipsum dolor sit amet,<br>ting elit, sed do eiusmod tdunt ut labore<br>et dolore magna aliqua. Ut enim ad<br>minim veniam,</p><a href="#">Read More</a>
</article>
<article class="card" style="left:440px">
  <svg class="quote-badge" viewBox="0 0 50 50"><rect width="50" height="50" fill="#1b7f8c"/><path d="M14 32v-8c0-5 3-8 7-8v4c-2 0-3 1-3 4h3v8zM28 32v-8c0-5 3-8 7-8v4c-2 0-3 1-3 4h3v8z" fill="#fff"/></svg>
  <h4>Helen C</h4><p>Lorem ipsum dolor sit amet,<br>ting elit, sed do eiusmod tdunt ut labore<br>et dolore magna aliqua. Ut enim ad<br>minim veniam,</p><a href="#">Read More</a>
</article>
<article class="card" style="left:789px">
  <svg class="quote-badge" viewBox="0 0 50 50"><rect width="50" height="50" fill="#1b7f8c"/><path d="M14 32v-8c0-5 3-8 7-8v4c-2 0-3 1-3 4h3v8zM28 32v-8c0-5 3-8 7-8v4c-2 0-3 1-3 4h3v8z" fill="#fff"/></svg>
  <h4>Jann O</h4><p>Lorem ipsum dolor sit amet,<br>ting elit, sed do eiusmod tdunt ut labore<br>et dolore magna aliqua. Ut enim ad<br>minim veniam,</p><a href="#">Read More</a>
</article>

<section class="gallery">
  <h2 class="section-title gallery-title">PROJECT GALLERY</h2>
  <div class="tile" style="left:89px;top:170px;background:linear-gradient(160deg,#4d8fd6,#c86a2e 60%,#5a6f8a)" role="img" aria-label="Line worker on a utility pole"></div>
  <div class="tile" style="left:347px;top:170px;background:linear-gradient(150deg,#2b2b2e,#9a7a6a 50%,#3b5fa0)" role="img" aria-label="Close-up of audio video connectors"></div>
  <div class="tile" style="left:607px;top:170px;background:linear-gradient(150deg,#dfe3e6,#a9b4bb 60%,#4a4f55)" role="img" aria-label="Technician setting up an office workstation"></div>
  <div class="tile" style="left:866px;top:170px;background:linear-gradient(150deg,#1d1f24,#4c5058 55%,#8a4a62)" role="img" aria-label="Fusion splicing machine in use"></div>
  <div class="tile" style="left:89px;top:477px;background:linear-gradient(150deg,#2a2d31,#6d7278 55%,#1c1e21)" role="img" aria-label="Bundle of network cables in a rack"></div>
  <div class="tile" style="left:347px;top:477px;background:linear-gradient(150deg,#efeeec,#c9a994 50%,#2d2d30)" role="img" aria-label="Hand holding glowing optical fibers"></div>
  <div class="tile" style="left:607px;top:477px;background:linear-gradient(150deg,#b58a5e,#d9cdb8 55%,#6e7f98)" role="img" aria-label="Meeting room with wall-mounted display"></div>
  <div class="tile" style="left:866px;top:477px;background:linear-gradient(150deg,#d8d4cf,#6fb64a 45%,#d05a2a)" role="img" aria-label="Colour-coded fiber optic connectors"></div>
  <a class="btn btn-teal abs view-all" href="#">View All</a>
</section>

<footer class="site-footer">
  <div class="footer-brand"><span class="brand-dot" style="background:#2a9aa8"></span>Kelmori</div>
  <nav class="footer-nav"><a href="#">Home</a><a href="#">About Us</a><a href="#">Services</a><a href="#">Work</a><a href="#">Solution</a><a href="#">Contact Us</a></nav>
  <div class="contact" style="left:113px">
    <div class="icon"><svg width="24" height="24" viewBox="0 0 24 24" fill="none" stroke="#bbb" stroke-width="1.6"><path d="M12 22s-7-7-7-12a7 7 0 0 1 14 0c0 5-7 12-7 12z"/><circle cx="12" cy="10" r="2.5"/></svg></div>
    48 Harbour Lane,<br>Pyrmont, Sydney Australia
  </div>
  <div class="contact" style="left:453px">
    <div class="icon is-active"><svg width="24" height="24" viewBox="0 0 24 24" fill="none" stroke="#fff" stroke-width="1.8"><path d="M5 3h4l2 5-3 2a11 11 0 0 0 6 6l2-3 5 2v4a2 2 0 0 1-2 2A17 17 0 0 1 3 5a2 2 0 0 1 2-2z"/></svg></div>
    02 - 55 - 0148
  </div>
  <div class="contact" style="left:795px">
    <div class="icon"><svg width="24" height="24" viewBox="0 0 24 24" fill="none" stroke="#bbb" stroke-width="1.6"><rect x="3" y="5" width="18" height="14" rx="1"/><path d="M3 6l9 7 9-7"/></svg></div>
    hello@kelmori.com.au
  </div>
  <p class="copyright">© 2020 Copyrights The Company Name.All Rights Reserved.Contact Us &nbsp;|&nbsp; Privacy Policy &nbsp;|&nbsp; Legal Terms</p>
</footer>

</body>
</html>
```